Business Card Design - Local Discount Club

Looking for a fun business card for a local discount club. One side should be the logo only and the other should be have :

Name
Title
Phone, Email
Website

```html
<!DOCTYPE html>
<html lang="en">
<head>
<meta charset="utf-8">
<title>The Harbor Perk Card – Business Card</title>
<link href="https://fonts.googleapis.com/css2?family=Montserrat:wght@400;500;800&display=swap" rel="stylesheet">
<style>
  :root {
    --page: #e9e9ec;
    --card: #1e1e1f;
    --blue: #3b57b5;
    --sky: #6cc7ea;
    --lime: #a7d15b;
    --ink: #f2f2f2;
    --muted: #cfcfd4;
  }
  * { margin: 0; padding: 0; box-sizing: border-box; }
  html, body { width: 1200px; height: 900px; overflow: hidden; }
  body {
    background: var(--page);
    font-family: "Montserrat", sans-serif;
    display: flex;
    flex-direction: column;
    align-items: center;
    justify-content: center;
    gap: 40px;
  }
  .card {
    position: relative;
    width: 700px;
    height: 400px;
    background: var(--card);
    border-radius: 4px;
    overflow: hidden;
    box-shadow: 0 10px 26px rgba(0,0,0,.22);
  }
  .stripe {
    position: absolute;
    left: 0; right: 0; bottom: 0;
    height: 14px;
    display: flex;
  }
  .stripe span:nth-child(1) { flex: 46; background: var(--blue); }
  .stripe span:nth-child(2) { flex: 32; background: var(--sky); }
  .stripe span:nth-child(3) { flex: 22; background: var(--lime); }

  .brand {
    display: flex;
    align-items: center;
    gap: 14px;
    color: var(--blue);
    font-weight: 800;
    text-transform: uppercase;
    letter-spacing: .02em;
    line-height: 1;
  }
  .brand-dot {
    border-radius: 50%;
    background: var(--blue);
    flex: none;
  }

  /* Logo side */
  .card-back .brand {
    position: absolute;
    top: 120px; left: 0; right: 0;
    justify-content: center;
    font-size: 46px;
  }
  .card-back .brand-dot { width: 26px; height: 26px; }
  .card-back .website {
    position: absolute;
    top: 262px; left: 0; right: 0;
    text-align: center;
    color: var(--ink);
    font-size: 17px;
    letter-spacing: .03em;
  }

  /* Info side */
  .card-front .brand {
    position: absolute;
    top: 48px; left: 150px;
    font-size: 28px;
  }
  .card-front .brand-dot { width: 18px; height: 18px; }
  .contacts {
    position: absolute;
    left: 40px; top: 165px;
    list-style: none;
    color: var(--ink);
    font-size: 15px;
  }
  .contacts li {
    display: flex;
    align-items: center;
    gap: 12px;
    margin-bottom: 8px;
  }
  .contacts svg { width: 14px; height: 14px; fill: var(--muted); flex: none; }
  .divider {
    position: absolute;
    left: 40px; right: 40px; top: 282px;
    height: 1.5px;
    background: var(--blue);
  }
  .person {
    position: absolute;
    right: 40px; top: 222px;
    text-align: right;
  }
  .person-name {
    color: var(--blue);
    font-weight: 800;
    font-size: 26px;
  }
  .person-title {
    color: var(--ink);
    font-size: 14px;
    margin-top: 2px;
  }
  .address {
    position: absolute;
    right: 40px; top: 298px;
    text-align: right;
    color: var(--ink);
    font-size: 15px;
    line-height: 1.4;
  }
</style>
</head>
<body>

  <section class="card card-back" aria-label="Card logo side">
    <div class="brand">
      <span class="brand-name">The Harbor Perk Card</span>
      <span class="brand-dot"></span>
    </div>
    <p class="website">www.harborperkcard.com</p>
    <div class="stripe"><span></span><span></span><span></span></div>
  </section>

  <section class="card card-front" aria-label="Card contact side">
    <div class="brand">
      <span class="brand-name">The Harbor Perk Card</span>
      <span class="brand-dot"></span>
    </div>

    <ul class="contacts">
      <li>
        <svg viewBox="0 0 24 24" aria-hidden="true"><path d="M6.6 10.8a15.1 15.1 0 0 0 6.6 6.6l2.2-2.2c.3-.3.7-.4 1-.2 1.1.4 2.3.6 3.6.6.6 0 1 .4 1 1V20c0 .6-.4 1-1 1A17 17 0 0 1 3 4c0-.6.4-1 1-1h3.5c.6 0 1 .4 1 1 0 1.3.2 2.5.6 3.6.1.3 0 .7-.2 1z"/></svg>
        <span>+49 401 555 0192</span>
      </li>
      <li>
        <svg viewBox="0 0 24 24" aria-hidden="true"><path d="M2 5h20v14H2z M4 7v.5l8 5 8-5V7l-8 5z" fill-rule="evenodd"/></svg>
        <span>hello@harborperkcard.com</span>
      </li>
      <li>
        <svg viewBox="0 0 24 24" aria-hidden="true"><path d="M12 2a10 10 0 1 0 0 20 10 10 0 0 0 0-20zm6.9 6h-3a15 15 0 0 0-1.3-4A8 8 0 0 1 18.9 8zM12 4c.8 1.1 1.5 2.5 1.9 4h-3.8c.4-1.5 1.1-2.9 1.9-4zM4.3 14a8 8 0 0 1 0-4h3.4a16 16 0 0 0 0 4zm.8 2h3a15 15 0 0 0 1.3 4A8 8 0 0 1 5.1 16zm3-8h-3a8 8 0 0 1 4.3-4A15 15 0 0 0 8.1 8zM12 20c-.8-1.1-1.5-2.5-1.9-4h3.8c-.4 1.5-1.1 2.9-1.9 4zm2.3-6H9.7a14 14 0 0 1 0-4h4.6a14 14 0 0 1 0 4zm.3 6a15 15 0 0 0 1.3-4h3a8 8 0 0 1-4.3 4zm1.7-6a16 16 0 0 0 0-4h3.4a8 8 0 0 1 0 4z"/></svg>
        <span>www.harborperkcard.com</span>
      </li>
    </ul>

    <div class="person">
      <p class="person-name">Adrian Cole</p>
      <p class="person-title">Owner</p>
    </div>

    <div class="divider"></div>

    <p class="address">Lindenweg 42<br>20095 Hamburg</p>

    <div class="stripe"><span></span><span></span><span></span></div>
  </section>

</body>
</html>
```